PulseLedgerPro.Com PowerPoint

I need a PowerPoint layout for my presentations. My business is called PulseLedgerPro.Com - my presentations teach cardiologists how to document their procedures and visits and teaches them how to bill accurately for them.

Industry/Entity Type

Business

Requirements
Must have
• the logo should be subtly there on each page - perhaps as a watermark? I'm really not creative; please help.

```html
<!DOCTYPE html>
<html lang="en">
<head>
<meta charset="utf-8">
<title>PulseLedgerPro.Com — Title Slide</title>
<link rel="stylesheet" href="https://fonts.googleapis.com/css2?family=Graduate&family=Open+Sans:wght@400;600&display=swap">
<style>
  :root {
    --page: #ffffff;
    --slide-light: #f3f3f3;
    --slide-mid: #e2e2e2;
    --slide-dark: #d4d4d4;
    --brand-red: #c1222d;
    --ink: #1b1b1b;
    --url-ink: #333333;
    --white: #ffffff;
  }
  html, body {
    margin: 0;
    padding: 0;
    width: 1200px;
    height: 900px;
    overflow: hidden;
    background: var(--page);
  }
  .canvas {
    position: relative;
    width: 1200px;
    height: 900px;
  }
  .slide {
    position: absolute;
    left: 27px;
    top: 163px;
    width: 1145px;
    height: 644px;
    overflow: hidden;
  }
  .slide-texture {
    position: absolute;
    inset: 0;
    background:
      radial-gradient(ellipse at 50% 35%, var(--slide-light) 0%, transparent 60%),
      linear-gradient(180deg, var(--slide-light) 0%, var(--slide-mid) 55%, var(--slide-dark) 100%);
  }
  .slide-art {
    position: absolute;
    inset: 0;
  }
  .title {
    font-family: "Graduate", "Rockwell", serif;
    fill: var(--brand-red);
  }
  .subtitle {
    font-family: "Open Sans", Arial, sans-serif;
    fill: var(--ink);
  }
  .reflection { opacity: 0.14; }
  .reflection .title { fill: #444; }
  .brand-name {
    font-family: "Graduate", "Rockwell", serif;
    fill: var(--brand-red);
  }
  .site-url {
    font-family: "Open Sans", Arial, sans-serif;
    fill: var(--url-ink);
  }
  .page-number {
    font-family: "Graduate", "Rockwell", serif;
    fill: var(--white);
  }
</style>
</head>
<body>
<main class="canvas">
  <section class="slide">
    <div class="slide-texture" role="img" aria-label="Soft grey crumpled paper texture background"></div>
    <svg class="slide-art" width="1145" height="644" viewBox="27 163 1145 644" xmlns="http://www.w3.org/2000/svg">
      <text class="title" x="290" y="308" font-size="118" textLength="598" lengthAdjust="spacingAndGlyphs">TITLE PAGE</text>
      <text class="subtitle" x="305" y="350" font-size="24" textLength="580" lengthAdjust="spacingAndGlyphs">DETAILS OF PRESENTATION / NAME OF PRESENTOR</text>

      <g class="reflection" transform="translate(0 712) scale(1 -1)">
        <text class="subtitle" x="305" y="350" font-size="24" textLength="580" lengthAdjust="spacingAndGlyphs">DETAILS OF PRESENTATION / NAME OF PRESENTOR</text>
      </g>
      <g class="reflection" transform="translate(0 704) scale(1 -1)">
        <text class="title" x="305" y="308" font-size="84" textLength="580" lengthAdjust="spacingAndGlyphs">TITLE PAGE</text>
      </g>

      <g class="brand-lockup">
        <circle cx="420" cy="588" r="24" fill="var(--brand-red)"/>
        <text class="brand-name" x="458" y="601" font-size="36" textLength="362" lengthAdjust="spacingAndGlyphs">PulseLedgerPro.Com</text>
      </g>

      <text class="site-url" x="610" y="771" font-size="26" text-anchor="middle">http://www.companysite.com/</text>

      <g class="page-marker">
        <polygon points="1047,785 1148,785 1148,684" fill="var(--brand-red)"/>
        <text class="page-number" x="1120" y="774" font-size="38" text-anchor="middle">01</text>
      </g>
    </svg>
  </section>
</main>
</body>
</html>
```